Project Quarter 2

A business card with the following details

Rob Kettering
Consultant/Speaker/Trainer

The Brand Quarter Hub (Insert Logo)
Insights and Tools for Brand Builders
www.brandquarterhub.com

Rob.Kettering@brandquarterhub.com
+61 452 918 604
Facebook icon
Twitter icon
Linkedin icon
Google+ icon
Pinterist icon

Target Market(s)

Small and Medium sized business owners
Brand marketers

Industry/Entity Type

Business

Requirements
Must have
• Utilise The Brand Quarter Hub Logo and colour scheme
Nice to have
• More male than female in outlook.
Have a connnected feel to it and a link to a precinct good too.
Bold and simple design the ideal

```html
<!DOCTYPE html>
<html lang="en">
<head>
<meta charset="utf-8">
<title>The Brand Quarter Hub – Business Card</title>
<link rel="stylesheet" href="https://fonts.googleapis.com/css2?family=Open+Sans:wght@400;700&display=swap">
<style>
  :root {
    --navy: #0b3f63;
    --teal: #2f8db0;
    --mist: #a3abba;
    --paper: #f4f5f6;
    --backdrop: #e9eaec;
    --social: #6f8aa3;
  }
  * { margin: 0; padding: 0; box-sizing: border-box; }
  html, body { width: 1200px; height: 955px; overflow: hidden; }
  body {
    background: var(--backdrop);
    font-family: "Open Sans", Arial, sans-serif;
    position: relative;
  }
  .card {
    position: absolute;
    top: 327px;
    width: 520px;
    height: 300px;
    border-radius: 3px;
    box-shadow: 0 6px 18px rgba(0,0,0,0.12);
    overflow: hidden;
  }
  .card--front { left: 50px; background: var(--paper); }
  .card--back { left: 630px; background: var(--navy); }

  /* Front: brand block */
  .brand {
    position: absolute;
    left: 0; right: 0; top: 56px;
    text-align: center;
  }
  .brand__row {
    display: inline-flex;
    align-items: center;
    gap: 10px;
  }
  .brand__dot {
    width: 30px; height: 30px;
    border-radius: 50%;
    background: var(--navy);
  }
  .brand__name {
    font-size: 27px;
    font-weight: 400;
    color: var(--teal);
    letter-spacing: -0.5px;
  }
  .brand__tagline {
    margin-top: 4px;
    font-size: 10.5px;
    color: var(--teal);
    letter-spacing: 0.3px;
  }

  /* Front: social squares */
  .social {
    position: absolute;
    right: 30px; top: 150px;
    display: flex; gap: 4px;
  }
  .social__item {
    width: 16px; height: 16px;
    border-radius: 2px;
    background: var(--social);
  }

  /* Front: contact block */
  .contact {
    position: absolute;
    left: 40px; top: 178px;
  }
  .contact__marker {
    position: absolute;
    left: -40px; top: 5px;
    width: 0; height: 0;
    border-top: 8px solid transparent;
    border-bottom: 8px solid transparent;
    border-left: 12px solid var(--navy);
  }
  .contact__name {
    font-size: 16px; font-weight: 700;
    color: var(--navy);
    line-height: 1.3;
  }
  .contact__role {
    font-size: 11px;
    color: var(--teal);
    margin-bottom: 6px;
  }
  .contact__line {
    display: flex; align-items: center; gap: 7px;
    font-size: 10.5px;
    color: var(--navy);
    line-height: 1.5;
  }
  .contact__icon { width: 11px; height: 11px; flex: none; }

  /* Back */
  .back__circle {
    position: absolute;
    right: 70px; top: 30px;
    width: 150px; height: 150px;
    border-radius: 50%;
    background: var(--mist);
  }
  .back__name {
    position: absolute;
    left: 40px; bottom: 40px;
    font-size: 28px;
    font-weight: 400;
    color: var(--mist);
    letter-spacing: -0.5px;
  }
</style>
</head>
<body>
  <section class="card card--front" aria-label="Business card front">
    <div class="brand">
      <div class="brand__row">
        <span class="brand__dot"></span>
        <span class="brand__name">thebrandquarterhub</span>
      </div>
      <p class="brand__tagline">Insights and Tools for Brand Builders</p>
    </div>

    <div class="social" aria-label="Social profiles">
      <span class="social__item"></span>
      <span class="social__item"></span>
      <span class="social__item"></span>
      <span class="social__item"></span>
      <span class="social__item"></span>
    </div>

    <div class="contact">
      <span class="contact__marker"></span>
      <p class="contact__name">Rob Kettering</p>
      <p class="contact__role">Consultant/Speaker/Trainer</p>
      <p class="contact__line">
        <svg class="contact__icon" viewBox="0 0 11 11"><rect width="11" height="11" rx="1.5" fill="#0b3f63"/><rect x="3.5" y="2" width="4" height="7" rx="0.8" fill="none" stroke="#fff" stroke-width="1"/></svg>
        +61 452 918 604
      </p>
      <p class="contact__line">
        <svg class="contact__icon" viewBox="0 0 11 11"><rect width="11" height="11" rx="1.5" fill="#0b3f63"/><rect x="2" y="3" width="7" height="5" fill="none" stroke="#fff" stroke-width="0.9"/><path d="M2 3 L5.5 6 L9 3" fill="none" stroke="#fff" stroke-width="0.9"/></svg>
        Rob.Kettering@brandquarterhub.com
      </p>
      <p class="contact__line">
        <svg class="contact__icon" viewBox="0 0 11 11"><rect width="11" height="11" rx="1.5" fill="#0b3f63"/><circle cx="5.5" cy="5.5" r="3.2" fill="none" stroke="#fff" stroke-width="0.9"/><path d="M2.3 5.5 H8.7" stroke="#fff" stroke-width="0.8"/></svg>
        www.brandquarterhub.com
      </p>
    </div>
  </section>

  <section class="card card--back" aria-label="Business card back">
    <span class="back__circle"></span>
    <p class="back__name">thebrandquarterhub</p>
  </section>
</body>
</html>
```